Design A Beginners Ketogenic Recipe Book Cover

I'm looking for a recipe book cover that looks professional, and incoporates "The Sunday Harvest Table Cookbook". I have plenty more recipe photos if needed, but would love a pro's take on the graphic design.

Its targeted at beginners of the ketogenic diet, and I would like it to highlight a similar design from my website and graphics found at https://www.brightmeadowhub.com.au/

Target Market(s)

American / Australian / Canadian Females - Ages from 35 - 50. Interested in weight loss, diets, ketogenic diet.

Industry/Entity Type

Cooking

Font styles to use
Serif

Colors
33a6d7
0692cd
85cae6
cee9f5

Requirements
Must have
• Must include my logo, must include title "The Sunday Harvest Table Cookbook"
Nice to have
• I don't have a strong idea for the cook book, but If you reseach cookbooks you'll get a good idea on what a cookbook should look like.

```html
<!DOCTYPE html>
<html lang="en">
<head>
<meta charset="utf-8">
<title>The Sunday Harvest Table Cookbook</title>
<link href="https://fonts.googleapis.com/css2?family=Parisienne&family=Marcellus+SC&family=Montserrat:wght@800&display=swap" rel="stylesheet">
<style>
  :root {
    --sky: #33a6d7;
    --ocean: #0692cd;
    --mist: #85cae6;
    --ice: #cee9f5;
    --paper: #ffffff;
    --ink: #1f6f96;
  }
  html, body {
    margin: 0;
    padding: 0;
    overflow: hidden;
    background: var(--paper);
  }
  .cover {
    position: relative;
    width: 841px;
    height: 1200px;
    background: var(--paper);
    overflow: hidden;
  }
  .photo {
    position: absolute;
    width: 384px;
  }
  .photo--cookies {
    left: 28px; top: 28px; height: 430px;
    background:
      radial-gradient(ellipse 62% 48% at 50% 60%, #d9ad73 0%, #c8935a 55%, rgba(200,147,90,0) 100%),
      linear-gradient(180deg, #ecebe8 0%, #dcd8d2 45%, #5a4a40 100%);
  }
  .photo--toast {
    left: 430px; top: 28px; height: 430px;
    background:
      radial-gradient(ellipse 55% 45% at 42% 52%, #d99a45 0%, #c7883a 50%, rgba(199,136,58,0) 100%),
      linear-gradient(180deg, #f6f5f3 0%, #eceae6 50%, #a9a9ab 100%);
  }
  .photo--bread {
    left: 28px; top: 722px; height: 450px;
    background:
      radial-gradient(ellipse 58% 42% at 42% 45%, #ecdcb4 0%, #e2c894 55%, rgba(226,200,148,0) 100%),
      linear-gradient(180deg, #e9e7e3 0%, #ded9d1 55%, #4a4039 100%);
  }
  .photo--eggs {
    left: 430px; top: 722px; height: 450px;
    background:
      radial-gradient(ellipse 50% 36% at 52% 62%, #e9b95a 0%, #e0aa4a 45%, rgba(224,170,74,0) 100%),
      radial-gradient(ellipse 30% 22% at 85% 85%, #7fa85f 0%, rgba(127,168,95,0) 100%),
      linear-gradient(180deg, #f6f6f5 0%, #eeece8 60%, #e4e2dd 100%);
  }
  .brand {
    position: absolute;
    left: 56px;
    top: 28px;
    width: 290px;
    height: 108px;
    background: var(--paper);
    display: flex;
    align-items: center;
    gap: 14px;
    padding-left: 10px;
    box-sizing: border-box;
  }
  .brand__mark {
    width: 90px;
    height: 90px;
    background: var(--sky);
    flex: none;
  }
  .brand__name {
    font-family: "Montserrat", sans-serif;
    font-weight: 800;
    font-size: 26px;
    line-height: 1.05;
    color: var(--ink);
    text-transform: uppercase;
  }
  .title {
    position: absolute;
    left: 0;
    top: 478px;
    width: 841px;
    text-align: center;
  }
  .title__script {
    font-family: "Parisienne", cursive;
    font-weight: 400;
    font-size: 88px;
    line-height: 1.1;
    color: var(--sky);
    margin: 0;
  }
  .title__band {
    width: 736px;
    height: 84px;
    margin: 8px auto 0;
    background: var(--sky);
    border-radius: 42px;
    box-shadow: inset 0 0 0 3px var(--paper), 0 0 0 2px var(--sky);
    font-family: "Marcellus SC", serif;
    font-size: 50px;
    line-height: 84px;
    letter-spacing: 1px;
    color: var(--paper);
  }
</style>
</head>
<body>
  <main class="cover">
    <div class="photo photo--cookies" role="img" aria-label="Stack of chocolate chip cookies on a dark board"></div>
    <div class="photo photo--toast" role="img" aria-label="Stack of french toast with syrup beside a cup of coffee"></div>
    <div class="photo photo--bread" role="img" aria-label="Loaf of almond bread on baking paper with scattered almonds"></div>
    <div class="photo photo--eggs" role="img" aria-label="Plate of fried egg and golden toast with basil"></div>

    <div class="brand">
      <div class="brand__mark"></div>
      <div class="brand__name">Bright<br>Meadow Hub</div>
    </div>

    <header class="title">
      <h1 class="title__script">The Sunday Harvest</h1>
      <div class="title__band">Table Cookbook</div>
    </header>
  </main>
</body>
</html>
```